Modern Business Card Design for Independent Urban Music Label

We need a card design for an independent urban music label called Copper Kite Records based in London. We develop and promote urban British music artists. We attend lots of high profile events with high profile industry people and want a card that comes across both on-brand and sophisticated, professional, trustworthy. I have attached our logo - please use the black and orange version in the upper left HOWEVER we are open to seeing other colors than the orange used though we want the shape of the logo to remain the same.

Info to please include:
Name
Position
Phone
Email
Website

Additional Info:
Twitter: @CopperKiteRecsUK
Insta: @CopperKiteRecs

Target Market(s)

Industry professionals and others artists

Industry/Entity Type

Business

Contact Information for Business Card

Info to please include:
Name
Position
Phone
Email
Website

Additional Info:
Twitter: @CopperKiteRecsUK
Insta: @CopperKiteRecs

Requirements
Must have
• Logo, company name
• Info to please include:
• Name
• Position
• Phone
• Email
• Website
Nice to have
• Twitter: @CopperKiteRecsUK
• Insta: @CopperKiteRecs
• If it can be done so that it doesn't look cluttered

```html
<!DOCTYPE html>
<html lang="en">
<head>
<meta charset="utf-8">
<title>Copper Kite Records – Business Card</title>
<link rel="stylesheet" href="https://fonts.googleapis.com/css2?family=Lato:wght@400;700&display=swap">
<style>
  :root {
    --backdrop: #e9e6e1;
    --card: #ffffff;
    --card-shade: #f1f1f1;
    --ink: #3a3a3a;
    --ink-soft: #5b5b5b;
    --copper: #f0a56c;
    --copper-deep: #e88a45;
    --ghost: #ececec;
  }
  * { box-sizing: border-box; margin: 0; padding: 0; }
  html, body { width: 1200px; height: 1023px; overflow: hidden; }
  body {
    background: var(--backdrop);
    font-family: "Lato", Arial, sans-serif;
    color: var(--ink);
    display: flex;
    flex-direction: column;
    align-items: center;
    justify-content: center;
    gap: 48px;
  }
  .card {
    position: relative;
    width: 770px;
    height: 440px;
    background: linear-gradient(160deg, var(--card) 55%, var(--card-shade));
    box-shadow: 0 10px 28px rgba(0,0,0,.18);
    overflow: hidden;
  }

  /* front */
  .front-swoosh { position: absolute; inset: 0; width: 100%; height: 100%; }
  .brand {
    position: absolute;
    display: flex;
    align-items: center;
    gap: 12px;
    font-weight: 700;
    text-transform: uppercase;
    letter-spacing: .14em;
    color: var(--copper);
  }
  .brand-dot {
    width: 16px; height: 16px; border-radius: 50%;
    background: var(--copper);
    flex: none;
  }
  .front .brand { left: 48px; top: 190px; font-size: 21px; width: 250px; line-height: 1.35; }
  .divider {
    position: absolute;
    left: 320px; top: 70px;
    width: 2px; height: 220px;
    background: var(--copper);
  }
  .contact-block { position: absolute; left: 360px; top: 62px; }
  .person-name { font-size: 30px; font-weight: 700; color: var(--copper); }
  .person-role { font-size: 20px; color: var(--ink-soft); margin-top: 4px; }
  .contact-list { list-style: none; margin-top: 22px; }
  .contact-list li {
    display: flex; align-items: center; gap: 14px;
    font-size: 20px; line-height: 1.55; color: var(--ink);
  }
  .icon { width: 18px; height: 18px; flex: none; }
  .icon-square { width: 16px; height: 16px; background: var(--ink); flex: none; margin: 0 1px; }

  /* back */
  .ghost-name {
    position: absolute;
    left: -20px; top: 40px;
    font-size: 132px; font-weight: 700;
    line-height: .95;
    text-transform: uppercase;
    color: var(--ghost);
    letter-spacing: .02em;
    white-space: nowrap;
  }
  .back .brand { right: 70px; top: 200px; font-size: 22px; }
  .back-handle {
    position: absolute; right: 70px; top: 250px;
    font-size: 19px; color: var(--ink);
  }
</style>
</head>
<body>

<section class="card front" aria-label="Card front">
  <svg class="front-swoosh" viewBox="0 0 770 440" preserveAspectRatio="none" aria-hidden="true">
    <path d="M0 430 C 260 330, 520 330, 770 380 L770 392 C 520 345, 260 345, 0 440 Z" fill="var(--copper)"/>
  </svg>

  <div class="brand"><span class="brand-dot"></span><span>Copper Kite Records</span></div>

  <div class="divider"></div>

  <div class="contact-block">
    <h1 class="person-name">Daniel Marsh</h1>
    <p class="person-role">Director</p>
    <ul class="contact-list">
      <li>
        <svg class="icon" viewBox="0 0 18 18" aria-hidden="true"><rect width="18" height="18" fill="var(--ink)"/><path d="M5 4h3l1 3-2 1a7 7 0 0 0 3 3l1-2 3 1v3c-6 0-9-3-9-9z" fill="#fff"/></svg>
        000 111 2122
      </li>
      <li>
        <svg class="icon" viewBox="0 0 18 18" aria-hidden="true"><rect width="18" height="18" fill="var(--ink)"/><rect x="3" y="5" width="12" height="8" fill="none" stroke="#fff" stroke-width="1.3"/><path d="M3 5l6 5 6-5" fill="none" stroke="#fff" stroke-width="1.3"/></svg>
        name@yourweb.com
      </li>
      <li>
        <svg class="icon" viewBox="0 0 18 18" aria-hidden="true"><circle cx="9" cy="9" r="8.5" fill="var(--ink)"/><circle cx="9" cy="9" r="5.5" fill="none" stroke="#fff" stroke-width="1.1"/><ellipse cx="9" cy="9" rx="2.4" ry="5.5" fill="none" stroke="#fff" stroke-width="1.1"/><path d="M3.5 9h11" stroke="#fff" stroke-width="1.1"/></svg>
        www.yourweb.com
      </li>
      <li><span class="icon-square"></span>@CopperKiteRecsUK</li>
      <li><span class="icon-square"></span>@CopperKiteRecs</li>
    </ul>
  </div>
</section>

<section class="card back" aria-label="Card back">
  <div class="ghost-name" aria-hidden="true">Copper<br>Kite</div>
  <div class="brand"><span class="brand-dot"></span><span>Copper Kite Records</span></div>
  <p class="back-handle">@CopperKiteRecsUK</p>
</section>

</body>
</html>
```